Harbor Loan Ad (8 x 8)

Bluegate Financial Services
Introduces

THE HARBOR LOAN

Interest Rates as low as 2.5%
640 Minimum Credit Score
Close in Only 22 Days

$100 per loan donated to Open Fields Unity Movement

Call (800) 555-0147 Today
Bluegate Financial Services, Inc.
4120 Marlow Lane, Linden Park, MD 20999
www.bluegatelend.example
NMLS #730618

(small print)
Up to 95% Loan to Value. Owner Occupied Only. Purchase or Rate & Term Only. All loans subject to Underwriter Approval.

```html
<!DOCTYPE html>
<html lang="en">
<head>
<meta charset="utf-8">
<title>Harbor Loan Ad</title>
<link rel="stylesheet" href="https://fonts.googleapis.com/css2?family=Montserrat:wght@300;400;500;600;700;800;900&display=swap">
<style>
  :root {
    --gold: #ad9b33;
    --gold-band: #a89a35;
    --ink: #111111;
    --black: #0b0b0b;
    --white: #ffffff;
    --rule: #6d6d6d;
    --badge: #4a4a4a;
  }
  html, body {
    margin: 0;
    padding: 0;
    width: 1200px;
    height: 1200px;
    overflow: hidden;
    background: var(--white);
    font-family: "Montserrat", sans-serif;
  }
  .ad {
    position: absolute;
    left: 290px;
    top: 290px;
    width: 576px;
    height: 576px;
    transform: scale(1.0909);
    transform-origin: 0 0;
    background: var(--black);
    overflow: hidden;
    color: var(--white);
  }
  .ad > * { position: absolute; }
  .top-band { left: 0; top: 0; width: 576px; height: 8px; background: var(--gold-band); }
  .hero-photo {
    left: 0; top: 8px; width: 576px; height: 568px;
    background:
      linear-gradient(180deg, #eef0f2 0%, #dfe3e6 18%, #b9c0c4 32%, #7f8c7c 48%, #4d5e3f 62%, #233018 74%, #0b0b0b 84%, #0b0b0b 100%);
  }
  .title {
    left: 32px; top: 22px; margin: 0;
    font-weight: 900; font-size: 37px; line-height: 41px;
    color: var(--ink); letter-spacing: -0.3px;
  }
  .subtitle {
    left: 32px; top: 111px; margin: 0;
    font-weight: 400; font-size: 21px; color: var(--ink); letter-spacing: 0.2px;
  }
  .brand {
    left: 410px; top: 40px; width: 150px;
    display: flex; align-items: center; gap: 8px;
    font-weight: 700; font-size: 13px; line-height: 16px; color: var(--ink);
  }
  .brand-dot { flex: none; width: 16px; height: 16px; border-radius: 50%; background: var(--ink); }
  .stat-figure { font-weight: 800; font-size: 50px; line-height: 1; letter-spacing: -1px; }
  .stat-label { font-weight: 600; font-size: 18px; line-height: 18px; }
  .stat-rate { left: 48px; top: 334px; }
  .stat-score { left: 214px; top: 334px; text-align: center; }
  .stat-rate .stat-label, .stat-score .stat-label { margin-top: 8px; }
  .rule { height: 1px; background: var(--rule); }
  .rule-top { left: 48px; top: 434px; width: 292px; }
  .rule-bottom { left: 48px; top: 459px; width: 292px; }
  .close-days { left: 57px; top: 438px; font-weight: 700; font-size: 14.5px; letter-spacing: 0.2px; }
  .donation {
    left: 360px; top: 318px; width: 173px; height: 148px;
    background: var(--gold); text-align: center;
  }
  .donation-amount { font-weight: 800; font-size: 52px; line-height: 1; margin-top: 10px; letter-spacing: -1px; }
  .donation-text { font-weight: 700; font-size: 15.5px; line-height: 16px; margin-top: 8px; padding: 0 10px; }
  .housing-badge { left: 26px; top: 480px; width: 66px; height: 62px; background: var(--badge); }
  .call-tag {
    left: 106px; top: 494px; width: 121px; height: 19px;
    background: var(--gold); color: var(--white);
    font-weight: 800; font-size: 11px; line-height: 19px; text-align: center;
  }
  .phone { left: 102px; top: 518px; display: flex; align-items: center; gap: 6px;
    font-weight: 800; font-size: 20px; white-space: nowrap; }
  .divider { left: 296px; top: 496px; width: 1px; height: 44px; background: var(--rule); }
  .address { left: 303px; top: 496px; display: flex; gap: 6px; font-size: 10.5px; line-height: 13px; font-weight: 400; white-space: nowrap; }
  .web { left: 309px; top: 526px; font-weight: 700; font-size: 10px; color: var(--gold); white-space: nowrap; }
  .fine-print { left: 0; top: 558px; width: 576px; margin: 0; text-align: center; font-size: 6.8px; font-weight: 500; }
</style>
</head>
<body>
  <main class="ad">
    <div class="hero-photo" role="img" aria-label="Photo of a house facade overlaid with a group of people raising fists"></div>
    <div class="top-band"></div>

    <h1 class="title">THE HARBOR<br>MORTGAGE LOAN</h1>
    <p class="subtitle">PURCHASES AND REFINANCES</p>

    <div class="brand"><span class="brand-dot"></span><span>Bluegate Financial Services</span></div>

    <div class="stat-rate">
      <div class="stat-figure">2.5%</div>
      <div class="stat-label">Interest Rates<br>as low as 2.5%</div>
    </div>
    <div class="stat-score">
      <div class="stat-figure">640</div>
      <div class="stat-label">Minimum<br>Credit Score</div>
    </div>

    <div class="rule rule-top"></div>
    <div class="close-days">CLOSE IN ONLY 22 DAYS</div>
    <div class="rule rule-bottom"></div>

    <div class="donation">
      <div class="donation-amount">$100</div>
      <div class="donation-text">$100 per loan donated to Open Fields Unity Movement</div>
    </div>

    <div class="housing-badge" aria-hidden="true"></div>

    <div class="call-tag">CALL US TODAY!</div>
    <div class="phone">
      <svg width="20" height="20" viewBox="0 0 24 24" aria-hidden="true">
        <path d="M6.6 10.8a15 15 0 0 0 6.6 6.6l2.2-2.2a1 1 0 0 1 1-.25 11.4 11.4 0 0 0 3.6.57 1 1 0 0 1 1 1V20a1 1 0 0 1-1 1A17 17 0 0 1 3 4a1 1 0 0 1 1-1h3.5a1 1 0 0 1 1 1c0 1.25.2 2.45.57 3.570a1 1 0 0 1-.25 1z" fill="none" stroke="#fff" stroke-width="1.8"/>
      </svg>
      <span>(800) 555-0147</span>
    </div>

    <div class="divider"></div>

    <div class="address">
      <svg width="12" height="17" viewBox="0 0 12 17" aria-hidden="true">
        <path d="M6 0a6 6 0 0 0-6 6c0 4.5 6 11 6 11s6-6.5 6-11a6 6 0 0 0-6-6zm0 8.3A2.3 2.3 0 1 1 6 3.7a2.3 2.3 0 0 1 0 4.6z" fill="#fff"/>
      </svg>
      <span>Bluegate Financial Services, Inc.<br>4120 Marlow Lane, Linden Park, MD 20999</span>
    </div>
    <div class="web">www.bluegatelend.example ~ NMLS #730618</div>

    <p class="fine-print">Up to 95% Loan to Value. Owner Occupied Only. Purchase or Rate &amp; Term Only. All loans subject to Underwriter Approval.</p>
  </main>
</body>
</html>
```